BRC Business cards

We are a medium sized property company based in London and require a logo, Business card which reflects a professional company and incorporates our catchy name.

Our statement is (Building for the future) we like colours such as royal blue, greens and light browns but will look at anything.

Contact Information for Business Card

Brookcrest Estates Limited
Unit 4, 15-17 Farrowby Lane
London
SE22 7QN

Web: www.brookcrestestates-example.com

Email: brookcrestltd@mailbox-example.com

Telephone: +44-208-555-0142
Fax: +44-208-555-0187

```html
<!DOCTYPE html>
<html lang="en">
<head>
<meta charset="utf-8">
<title>Brookcrest Estates Limited – Business Card</title>
<link href="https://fonts.googleapis.com/css2?family=Questrial&display=swap" rel="stylesheet">
<style>
  :root {
    --backdrop: #2a2a2a;
    --card-white: #f3f3f3;
    --navy: #0e2468;
    --navy-deep: #0a1c55;
    --ink: #1d1d1d;
    --ink-soft: #333333;
    --contact: #d3d9ea;
  }
  html, body {
    margin: 0;
    padding: 0;
    width: 1200px;
    height: 873px;
    overflow: hidden;
    background: var(--backdrop);
    font-family: "Questrial", sans-serif;
  }
  .stage {
    position: relative;
    width: 1200px;
    height: 873px;
  }
  .card {
    position: absolute;
    left: 410px;
    top: 126px;
    width: 380px;
    height: 620px;
    background: var(--card-white);
    overflow: hidden;
    box-shadow: 0 10px 30px rgba(0,0,0,0.5);
  }
  .card__holder {
    position: absolute;
    top: 44px;
    left: 0;
    width: 100%;
    text-align: center;
    color: var(--ink);
  }
  .card__name {
    margin: 0;
    font-size: 24px;
    font-weight: 400;
    letter-spacing: 0.5px;
  }
  .card__role {
    margin: 4px 0 0;
    font-size: 14px;
    color: var(--ink-soft);
  }
  .brand {
    position: absolute;
    top: 168px;
    left: 0;
    width: 100%;
    display: flex;
    flex-direction: column;
    align-items: center;
    gap: 14px;
    color: var(--navy);
  }
  .brand__square {
    width: 54px;
    height: 54px;
    background: var(--navy);
  }
  .brand__name {
    font-size: 20px;
    letter-spacing: 1.5px;
    text-transform: uppercase;
    text-align: center;
    line-height: 1.3;
  }
  .skyline {
    position: absolute;
    left: 0;
    top: 300px;
    width: 100%;
    height: 70px;
    background: linear-gradient(to bottom, rgba(14,36,104,0) 0%, rgba(14,36,104,0.55) 45%, var(--navy) 100%);
  }
  .card__band {
    position: absolute;
    left: 0;
    top: 370px;
    width: 100%;
    height: 250px;
    background: var(--navy);
  }
  .contact {
    list-style: none;
    margin: 0;
    padding: 0;
    position: absolute;
    left: 34px;
    top: 386px;
    right: 20px;
    color: var(--contact);
    font-size: 15px;
  }
  .contact__item {
    display: flex;
    align-items: center;
    gap: 16px;
    height: 40px;
  }
  .contact__item--address {
    height: 54px;
    align-items: center;
  }
  .contact__icon {
    width: 26px;
    height: 26px;
    flex: none;
    fill: var(--contact);
  }
  .contact__text {
    line-height: 1.4;
    white-space: nowrap;
  }
</style>
</head>
<body>
<main class="stage">
  <article class="card">
    <header class="card__holder">
      <h1 class="card__name">Daniel K, Ashworth</h1>
      <p class="card__role">Broker/Owner</p>
    </header>

    <div class="brand">
      <span class="brand__square"></span>
      <span class="brand__name">Brookcrest<br>Estates Limited</span>
    </div>

    <div class="skyline" role="img" aria-label="Navy city skyline silhouette rising into the contact band"></div>
    <div class="card__band"></div>

    <ul class="contact">
      <li class="contact__item">
        <svg class="contact__icon" viewBox="0 0 26 26" aria-hidden="true">
          <rect x="7" y="2" width="12" height="22" rx="2" fill="none" stroke="#d3d9ea" stroke-width="2"/>
          <rect x="9" y="5" width="8" height="14" />
        </svg>
        <span class="contact__text">+44-208-555-0142</span>
      </li>
      <li class="contact__item">
        <svg class="contact__icon" viewBox="0 0 26 26" aria-hidden="true">
          <path d="M3 9 Q13 2 23 9 L20 12 L17 10 L9 10 L6 12 Z"/>
          <rect x="6" y="13" width="14" height="10" rx="2"/>
        </svg>
        <span class="contact__text">+44-208-555-0187</span>
      </li>
      <li class="contact__item">
        <svg class="contact__icon" viewBox="0 0 26 26" aria-hidden="true">
          <rect x="2" y="6" width="22" height="15" />
          <path d="M2 6 L13 15 L24 6" fill="none" stroke="#0e2468" stroke-width="1.8"/>
        </svg>
        <span class="contact__text">brookcrestltd@mailbox-example.com</span>
      </li>
      <li class="contact__item">
        <svg class="contact__icon" viewBox="0 0 26 26" aria-hidden="true">
          <circle cx="13" cy="13" r="11"/>
          <circle cx="13" cy="13" r="8" fill="#0e2468"/>
          <path d="M9 8 Q12 7 13 10 Q11 13 14 15 L12 19 Q8 16 9 8 Z M15 7 Q19 9 19 13 L16 12 Z"/>
        </svg>
        <span class="contact__text">www.brookcrestestates-example.com</span>
      </li>
      <li class="contact__item contact__item--address">
        <svg class="contact__icon" viewBox="0 0 26 26" aria-hidden="true">
          <path d="M13 2 C8 2 5 6 5 10 C5 16 13 24 13 24 C13 24 21 16 21 10 C21 6 18 2 13 2 Z"/>
          <circle cx="13" cy="10" r="3" fill="#0e2468"/>
        </svg>
        <span class="contact__text">Unit 4, 15-17 Farrowby Lane<br>London SE22 7QN</span>
      </li>
    </ul>
  </article>
</main>
</body>
</html>
```